Business Card Design Project

We have a logo, but would like to expand the use of it into a business card design. We are a B2B technology exchange platform for institutional investors to invest excess cash into short term assets matching their credit and pricing parameters. The assets are fractionalized and investors invest in portions.

Our customers are large, institutional, financial companies who are a bit traditional. We are high energy rebels with a cause...we are a disruptive technology and want to be viewed as a game changer but we need to present an image of trustworthiness and secure.

We are open not only to the image design but the material, die cut, etc. but want to stay in the traditional size of a business card.

We have other formats of the logo if needed. Our website is www.brambleharbor.com
Updates

I have posted a powerpoint template that we have been using.  This should not be considered the template we will use (after business cards we will have another project to incorporate business card design into powerpoint template) but just to give you a flavor of where we have been and have used in the past.

Target Market(s)

Institutional investors, asset managers, large fund institutions

Industry/Entity Type

Financial

Requirements
Must have
• Our logo
Traditional size
Nice to have
• unique use of logo, unique material, die cut, etc
Crisp, clean look
Use of both sides of card in a creative manner

```html
<!DOCTYPE html>
<html lang="en">
<head>
<meta charset="utf-8">
<title>Bramble Harbor – Business Cards</title>
<link href="https://fonts.googleapis.com/css2?family=Arimo:wght@400;700&display=swap" rel="stylesheet">
<style>
  :root{
    --bg:#e9e7e4;
    --orange:#f0a23c;
    --orange-light:#f8c57e;
    --orange-text:#e88a14;
    --grey-text:#6b6b6b;
    --ink:#1d1d1d;
    --blue-dark:#1e4f9c;
    --blue-light:#2aa6dc;
    --card-white:#fbfbfb;
  }
  *{margin:0;padding:0;box-sizing:border-box}
  html,body{width:1200px;height:995px;overflow:hidden}
  body{background:var(--bg);font-family:"Arimo",Arial,sans-serif;position:relative}
  .card{position:absolute;width:700px;height:400px;box-shadow:0 8px 24px rgba(0,0,0,.18);overflow:hidden}
  .card-front{left:110px;top:70px;background:linear-gradient(160deg,var(--orange-light) 0%,var(--orange) 70%,#eb9a35 100%)}
  .card-back{left:390px;top:520px;background:var(--card-white)}
  .front-swoosh{position:absolute;inset:0}
  .front-brand{position:absolute;left:60px;top:70px;display:flex;align-items:center;gap:14px}
  .front-brand .brand-name{font-weight:700;font-size:38px;letter-spacing:1px;color:var(--grey-text);text-transform:uppercase}
  .front-brand .brand-dot{width:30px;height:30px;border-radius:50%;background:var(--orange-text)}
  .back-brand{position:absolute;left:60px;top:50px;display:flex;align-items:center;gap:12px}
  .back-brand .brand-name{font-weight:700;font-size:34px;letter-spacing:1px;color:var(--grey-text);text-transform:uppercase}
  .back-brand .brand-dot{width:26px;height:26px;border-radius:50%;background:var(--orange-text)}
  .back-wave{position:absolute;left:0;top:190px;width:700px;height:60px}
  .holder{position:absolute;right:40px;top:112px;text-align:right}
  .holder-name{font-weight:700;font-size:26px;letter-spacing:2px;color:var(--orange-text)}
  .holder-title{font-size:19px;color:var(--ink);margin-top:8px}
  .address{position:absolute;left:60px;top:255px;font-size:14px;font-style:normal;letter-spacing:1.5px;line-height:24px;color:var(--ink)}
  .label{color:var(--orange-text)}
  .address .label{font-size:16px}
  .contacts{position:absolute;left:400px;top:255px;font-size:14px;letter-spacing:1px;line-height:24px;color:var(--ink);list-style:none}
  .contacts .web{letter-spacing:3px}
  .contacts .web .accent{color:var(--orange-text)}
</style>
</head>
<body>
  <section class="card card-front" aria-label="Card front">
    <svg class="front-swoosh" viewBox="0 0 700 400" preserveAspectRatio="none" aria-hidden="true">
      <path d="M0 40 Q250 200 700 180" fill="none" stroke="rgba(255,255,255,.25)" stroke-width="2"/>
      <path d="M0 250 Q300 330 700 230 L700 400 L0 400 Z" fill="rgba(230,140,40,.25)"/>
    </svg>
    <div class="front-brand"><span class="brand-dot"></span><span class="brand-name">Bramble Harbor</span></div>
  </section>

  <section class="card card-back" aria-label="Card back">
    <div class="back-brand"><span class="brand-dot"></span><span class="brand-name">Bramble Harbor</span></div>
    <div class="holder">
      <p class="holder-name">Martin Ellery</p>
      <p class="holder-title">President &amp; CEO</p>
    </div>
    <svg class="back-wave" viewBox="0 0 700 60" preserveAspectRatio="none" aria-hidden="true">
      <path d="M0 12 C200 12 300 40 400 30 C500 20 600 22 700 28 L700 40 C600 34 500 34 400 42 C300 50 200 26 0 26 Z" fill="var(--blue-light)"/>
      <path d="M0 26 C200 26 300 50 400 42 C500 34 600 34 700 40 L700 48 C600 44 500 44 400 50 C300 56 200 32 0 32 Z" fill="var(--blue-dark)"/>
    </svg>
    <address class="address">
      <span class="label">Address :</span><br>
      1820 Harbor Crest Lane<br>
      Suite 14, Alder Bay, CA 90210
    </address>
    <ul class="contacts">
      <li><span class="label">P:</span> 555.210.4831</li>
      <li><span class="label">C:</span> 555.306.7712</li>
      <li><span class="label">E:</span> martinellery@brambleharbor.com</li>
      <li><span class="label">Profile :</span> martinellery</li>
      <li class="web"><span class="label">W:</span> www.<span class="accent">BrambleHarbor</span>.com</li>
    </ul>
  </section>
</body>
</html>
```